Maplerise Trading Inc. needs an innovative idea for letterhead and visiting cards.

Maplerise Trading Inc. is a Canadian brand since 2007. It is a renown dealer of kids and office furniture locally. Moreover, exporting electric fixtures e.g. switches, LED's, down-lights etc. to Middle East and Africa. We have initiated a number of steps including re-branding, to boost our export in 2020. We have successfully designed our new logo a few months ago through 'Artfolio' and now we are looking for an innovative idea for a letterhead.
Some key points:
• Red, black and white are the three colors used in all our packaging and furniture. (grey is optional)
• Shouldn’t be too wide.
• Use of watermark is preferable.
• You can visit our North American site at www.mapleriseinc.com. Export website of the company will be launched soon. www.mapleriseinc.ca
• Same letterhead will be used locally and internationally.
• Our new logo and sample packaging is attached.

```html
<!DOCTYPE html>
<html lang="en">
<head>
<meta charset="utf-8">
<title>Maplerise Trading – Stationery</title>
<link href="https://fonts.googleapis.com/css2?family=Lato:wght@400;700&family=Open+Sans:wght@400;600&display=swap" rel="stylesheet">
<style>
  :root{
    --brand-red:#9b0b10;
    --ink:#3d3d3d;
    --grey:#4a4a4c;
    --paper:#ffffff;
    --backdrop:#e4e4e4;
  }
  *{margin:0;padding:0;box-sizing:border-box}
  html,body{width:1200px;height:1200px;overflow:hidden;background:var(--backdrop)}
  .stationery{position:relative;width:1200px;height:1200px}

  .brand{display:flex;align-items:center;gap:8px;font-family:"Lato",sans-serif;font-weight:700;color:var(--brand-red);white-space:nowrap}
  .brand-square{background:var(--brand-red);display:block}

  /* Letterhead */
  .letterhead{position:absolute;left:119px;top:278px;width:556px;height:715px;background:var(--paper);overflow:hidden;box-shadow:0 2px 6px rgba(0,0,0,.18)}
  .letterhead .brand{position:absolute;left:52px;top:28px;font-size:24px}
  .letterhead .brand-square{width:34px;height:34px}
  .letter-body{position:absolute;left:52px;top:129px;width:450px;font-family:"Open Sans",sans-serif;font-size:8.8px;line-height:16px;color:var(--ink)}
  .letter-body p{margin-bottom:16px;text-align:justify}
  .issue-date{margin-bottom:10px}
  .recipient{line-height:11px;margin-bottom:32px}
  .greeting{margin-bottom:16px}
  .closing{margin-top:24px}
  .signature{width:128px;height:16px;margin:6px 0 8px;background:linear-gradient(90deg,#d8d8d8,#efefef)}
  .signer-name{font-size:11px;font-weight:600;color:#333;line-height:14px}
  .signer-role{font-size:8.8px;line-height:16px}

  /* Footer bands: straight stacked rules */
  .footer-band{position:absolute;left:0;right:0;bottom:0;background:var(--brand-red)}
  .footer-band::before{content:"";position:absolute;left:0;right:0;top:-12px;height:6px;background:var(--grey)}
  .footer-band::after{content:"";position:absolute;left:0;right:0;top:6px;height:2px;background:#fff}
  .letterhead .footer-band{height:96px}

  .letter-contact{position:absolute;right:48px;bottom:20px;text-align:right;font-family:"Lato",sans-serif;color:#fff;font-size:10px;line-height:11px}
  .letter-contact .address{margin-top:8px;font-size:10.5px}
  .icon{display:inline-block;width:8px;height:8px;margin-left:2px;vertical-align:-1px}

  /* Envelope front */
  .envelope-front{position:absolute;left:715px;top:492px;width:432px;height:216px;background:var(--paper);overflow:hidden;box-shadow:0 2px 6px rgba(0,0,0,.18)}
  .envelope-front .brand{position:absolute;left:20px;top:22px;font-size:17px;gap:6px}
  .envelope-front .brand-square{width:25px;height:25px}
  .envelope-front .footer-band{height:46px}
  .envelope-front .footer-band::before{top:-9px;height:4px}
  .envelope-front .footer-band::after{top:5px;height:1.5px}
  .envelope-address{position:absolute;right:34px;bottom:16px;font-family:"Lato",sans-serif;font-size:7.5px;color:#fff}

  /* Envelope back */
  .envelope-back{position:absolute;left:717px;top:743px;width:429px;height:213px;background:var(--paper);box-shadow:0 2px 6px rgba(0,0,0,.18)}
  .envelope-flap{position:absolute;left:0;top:0;width:429px;height:51px}
  .envelope-back .brand{position:absolute;left:0;right:0;top:17px;justify-content:center;color:#fff;font-size:13px}
  .envelope-web{position:absolute;left:0;right:0;bottom:23px;text-align:center;font-family:"Lato",sans-serif;font-size:7.5px;color:var(--brand-red)}
</style>
</head>
<body>
<main class="stationery">

  <article class="letterhead">
    <div class="brand"><span class="brand-square"></span>Maplerise Trading</div>

    <div class="letter-body">
      <div class="issue-date">Issuing Date: May 5, 2018</div>
      <div class="recipient">Name Of Employee Mr. XYZABC<br>Address of Employee<br>Address Line 2 etc..</div>
      <div class="greeting">Dear Mr.XYZABC</div>
      <p>Lorem Ipsum has been the industry's standard dummy text ever since the 1500s, when an unknown printer took a galley of type and scrambled it to make a type specimen book. It has survived not only five centuries, but also the leap into electronic typesetting, remaining essentially unchanged. It was popularised in the 1960s with the release of Letraset sheets containing Lorem Ipsum passages, and more recently with desktop publishing software like Aldus PageMaker including versions of Lorem Ipsum.</p>
      <p>Lorem Ipsum is simply dummy text of the printing and typesetting industry. Lorem Ipsum has been the industry's standard dummy text ever since the 1500s, when an unknown printer took a galley of type and scrambled it to make a type specimen book.</p>
      <p>It has survived not only five centuries, but also the leap into electronic typesetting, remaining essentially unchanged. It was popularised in the 1960s with the release of Letraset sheets containing Lorem IpsumIpsum passages.</p>
      <div class="closing">Yours Sincerely</div>
      <div class="signature" role="img" aria-label="Handwritten signature of Daniel Mercer"></div>
      <div class="signer-name">Daniel Mercer</div>
      <div class="signer-role">Managing Director</div>
    </div>

    <div class="footer-band"></div>
    <div class="letter-contact">
      044-555 010 274<svg class="icon" viewBox="0 0 10 10"><path d="M1 3 Q5 0 9 3 L8 5 L6 4 L4 4 L2 5 Z M2 6 H8 V9 H2 Z" fill="#fff"/></svg><br>
      info@mapleriseinc.com<svg class="icon" viewBox="0 0 10 10"><rect x="0.5" y="2" width="9" height="6" fill="#fff"/><path d="M0.5 2 L5 5.5 L9.5 2" fill="none" stroke="var(--brand-red)" stroke-width="0.8"/></svg><br>
      www.mapleriseinc.com<svg class="icon" viewBox="0 0 10 10"><circle cx="5" cy="5" r="4.5" fill="#fff"/></svg>
      <div class="address">421, Address line here Country Name, 45452</div>
    </div>
  </article>

  <section class="envelope-front">
    <div class="brand"><span class="brand-square"></span>Maplerise Trading</div>
    <div class="footer-band"></div>
    <div class="envelope-address">421, Address line goes here Country Name, 45452</div>
  </section>

  <section class="envelope-back">
    <svg class="envelope-flap" viewBox="0 0 429 51" preserveAspectRatio="none">
      <path d="M0 0 H429 L413 51 H16 Z" fill="var(--brand-red)"/>
    </svg>
    <div class="brand">Maplerise Trading</div>
    <div class="envelope-web">www.mapleriseinc.com</div>
  </section>

</main>
</body>
</html>
```